UK Glass Restoration Company needs a Direct Mail Postcard Design

We need a HARD HITTING, COMPELLING 300dpi Camera Ready double sided postcard.
The dimensions will be 109mm x 152mm including bleed. We are a scratched glass repair / etched graffiti removal glass restoration company based in London, UK.
We operate mainly within the construction and commercial marketplace, however this particular postcard design is aimed solely at shop owners who have become victims of vandalism, due to etched graffiti tags and or scratches being left on their shop front glass.
We wish to focus the shop / business owners mind to the negative impact such vandalism has on the image of their business and how we are able to offer a quick and cost effective solution
We will supply text for both sides of the postcard along with relevant images, company logo and previous flyer designs, however we are happy for the selected designer to source suitable alternative images provided they are in keeping with the exact "Before" and "After" theme.
The finished postcard must preferably have a white background, but again we are open to creative suggestions.
Target Market(s)
UK SHOP OWNERS
Industry/Entity Type
It Company

```html
<!DOCTYPE html>
<html lang="en">
<head>
<meta charset="utf-8">
<title>Lucent Glass Repairs – Postcard</title>
<link rel="stylesheet" href="https://fonts.googleapis.com/css2?family=Didact+Gothic&family=Montserrat:wght@600;700&display=swap">
<style>
  :root {
    --page: #ffffff;
    --photo-top: #2f5266;
    --photo-bottom: #22404f;
    --panel: #1d4f6d;
    --band: #0e2638;
    --fold-grey: #a7acb1;
    --fold-white: #ffffff;
    --text: #ffffff;
    --brand: #3ea3db;
  }
  * { box-sizing: border-box; margin: 0; padding: 0; }
  html, body { width: 878px; height: 1200px; overflow: hidden; background: var(--page); }
  .canvas { position: relative; width: 878px; height: 1200px; }

  .postcard {
    position: absolute;
    top: 328px;
    width: 310px;
    height: 432px;
    transform-origin: 0 0;
    transform: scale(1.258);
    overflow: hidden;
    color: var(--text);
    font-family: "Didact Gothic", "Century Gothic", sans-serif;
  }
  .postcard--front { left: 29px; }
  .postcard--back { left: 459px; }

  .postcard__art { position: absolute; inset: 0; width: 310px; height: 432px; }

  .headline {
    position: absolute;
    left: 18px;
    top: 20px;
    font-family: "Montserrat", sans-serif;
    font-weight: 600;
    font-size: 17px;
    line-height: 21px;
    letter-spacing: 0.2px;
    text-transform: uppercase;
  }

  .section-title {
    position: absolute;
    font-family: "Montserrat", sans-serif;
    font-weight: 600;
    font-size: 10px;
    letter-spacing: 0.3px;
    text-transform: uppercase;
  }
  .postcard--front .section-title { left: 18px; top: 240px; }
  .postcard--back .section-title { right: 48px; top: 230px; font-size: 10.5px; }

  .intro {
    position: absolute;
    left: 18px;
    top: 262px;
    width: 270px;
    font-size: 9.2px;
    line-height: 12.6px;
  }
  .intro strong { font-family: "Montserrat", sans-serif; font-weight: 600; }

  .benefits {
    position: absolute;
    left: 10px;
    top: 250px;
    width: 292px;
    list-style: none;
    font-size: 6.6px;
    line-height: 8.4px;
  }
  .benefits li { position: relative; padding-left: 9px; margin-bottom: 7px; }
  .benefits li::before {
    content: "";
    position: absolute;
    left: 0;
    top: 2px;
    width: 4px;
    height: 4px;
    border-radius: 50%;
    background: var(--text);
  }
  .benefits li.benefits__item--inset { margin-left: 72px; }

  .contact {
    position: absolute;
    left: 18px;
    top: 392px;
    list-style: none;
    font-size: 8px;
    line-height: 12px;
  }
  .contact li { display: flex; align-items: center; gap: 5px; }
  .contact svg { width: 8px; height: 8px; flex: none; }

  .brand {
    position: absolute;
    right: 22px;
    top: 392px;
    display: flex;
    align-items: center;
    gap: 4px;
    color: var(--brand);
    font-size: 21px;
    line-height: 1;
  }
  .brand__dot {
    width: 7px;
    height: 7px;
    border-radius: 50%;
    background: var(--brand);
  }
</style>
</head>
<body>
<main class="canvas">

  <!-- Front side -->
  <section class="postcard postcard--front" aria-label="Postcard front">
    <svg class="postcard__art" viewBox="0 0 310 432" aria-hidden="false">
      <defs>
        <linearGradient id="shopWindowFront" x1="0" y1="0" x2="1" y2="1">
          <stop offset="0" stop-color="#365a6e"/>
          <stop offset="1" stop-color="#1f3c4c"/>
        </linearGradient>
      </defs>
      <rect width="310" height="215" fill="url(#shopWindowFront)" role="img" aria-label="Photo of a shop window with framed displays behind the glass"/>
      <polygon points="135,182 310,104 310,132" fill="var(--fold-grey)"/>
      <polygon points="165,184 310,130 310,200" fill="var(--fold-white)"/>
      <polygon points="0,182 165,184 310,222 310,432 0,432" fill="var(--panel)"/>
      <polygon points="0,342 310,368 310,432 0,432" fill="var(--band)"/>
    </svg>

    <h1 class="headline">Don't<br>let vandals<br>wreck your<br>image!</h1>

    <h2 class="section-title">Before repair – a bad first impression</h2>
    <p class="intro">What's on display in your shop window?<br>If it's graffiti, vandalism, or just wear and tear that's the first impression your customers get and it's not good. Lucent Glass Repairs remove damage from glass windows, making them sparkling clear – without replacing the glass! Our glass repair work is effective, green, and very economical. See our coupon on the other side to save even more! Call now for expert <strong>advice: 0800 555 0147</strong></p>

    <ul class="contact">
      <li><svg viewBox="0 0 10 10"><circle cx="5" cy="5" r="5" fill="#fff"/><path d="M3.3 2.6l1 1-.5.7a3.5 3.5 0 0 0 1.9 1.9l.7-.5 1 1-.7.8C4.9 7.3 2.7 5.1 2.5 3.3z" fill="var(--band)"/></svg>0800 555 0147</li>
      <li><svg viewBox="0 0 10 10"><circle cx="5" cy="5" r="4.3" fill="none" stroke="#fff" stroke-width="1"/><ellipse cx="5" cy="5" rx="1.8" ry="4.3" fill="none" stroke="#fff" stroke-width=".8"/><line x1=".7" y1="5" x2="9.3" y2="5" stroke="#fff" stroke-width=".8"/></svg>www.lucentglassrepairs.co.uk</li>
    </ul>
    <div class="brand"><span class="brand__name">Lucent</span><span class="brand__dot"></span></div>
  </section>

  <!-- Back side -->
  <section class="postcard postcard--back" aria-label="Postcard back">
    <svg class="postcard__art" viewBox="0 0 310 432" aria-hidden="false">
      <defs>
        <linearGradient id="shopWindowBack" x1="0" y1="0" x2="1" y2="1">
          <stop offset="0" stop-color="#365a6e"/>
          <stop offset="1" stop-color="#1f3c4c"/>
        </linearGradient>
      </defs>
      <rect width="310" height="215" fill="url(#shopWindowBack)" role="img" aria-label="Photo of a clean, clear shop window after repair"/>
      <polygon points="160,176 310,98 310,124" fill="var(--fold-grey)"/>
      <polygon points="195,180 310,122 310,192" fill="var(--fold-white)"/>
      <polygon points="0,176 195,180 310,212 310,432 0,432" fill="var(--panel)"/>
      <polygon points="0,380 310,356 310,432 0,432" fill="var(--band)"/>
    </svg>

    <h1 class="headline">After repair<br>clear as<br>new!</h1>

    <h2 class="section-title">Why Lucent Glass Repairs?</h2>
    <ul class="benefits">
      <li>We repair most shop window glass!<br>We repair laminated, tempered, toughened mirrored, tinted, and even ballistic glass.</li>
      <li class="benefits__item--inset">We repair curved glass! Don't replace expensive curved panes – get the like-new look for less by repairing.</li>
      <li>Finer work! We remove etched graffiti tags, scratches mineral deposits, and acid etched graffiti damage.</li>
      <li class="benefits__item--inset">Edge expertise! We can repair even deep scratches as close as 20mm from the edge of the glass.</li>
      <li>Save time and money! Typical savings of up to 80% over the cost of glass replacement, with zero downtime during repair.</li>
    </ul>

    <ul class="contact">
      <li><svg viewBox="0 0 10 10"><circle cx="5" cy="5" r="5" fill="#fff"/><path d="M3.3 2.6l1 1-.5.7a3.5 3.5 0 0 0 1.9 1.9l.7-.5 1 1-.7.8C4.9 7.3 2.7 5.1 2.5 3.3z" fill="var(--band)"/></svg>0800 555 0147</li>
      <li><svg viewBox="0 0 10 10"><circle cx="5" cy="5" r="4.3" fill="none" stroke="#fff" stroke-width="1"/><ellipse cx="5" cy="5" rx="1.8" ry="4.3" fill="none" stroke="#fff" stroke-width=".8"/><line x1=".7" y1="5" x2="9.3" y2="5" stroke="#fff" stroke-width=".8"/></svg>www.lucentglassrepairs.co.uk</li>
    </ul>
    <div class="brand"><span class="brand__name">Lucent</span><span class="brand__dot"></span></div>
  </section>

</main>
</body>
</html>
```